Business Card Design Project

Corwen Property Management

Our Business is residential property management, we therefore need a card that displays a professional image, but is clear and concise, and easy to read
Updates

We are committed now guys and girls, loving what we are seeing so far! 

Target Market(s)

Landlords, Rental Property Owners

Industry/Entity Type

Residential

Requirements
Must have
• Dean Fosterly - Principal
Tessa Fosterly - Director (Property Management)

PO Box 718
Holloway SA 5093

Dean: 0419 372 508
Tessa: 0419 613 947

www.corwenpropertymanagement.com.au
admin@corwenpropertymanagement.com.au

Nice to have
• I would like the card to be double sided, white background on the information side and then colour on the reverse, in blue or black and incorporating our logo

```html
<!DOCTYPE html>
<html lang="en">
<head>
<meta charset="utf-8">
<title>Corwen Property Management – Business Card</title>
<link rel="stylesheet" href="https://fonts.googleapis.com/css2?family=Source+Sans+3:wght@400;600;700&display=swap">
<style>
  :root {
    --backdrop: #e8e4de;
    --card-white: #ffffff;
    --charcoal: #5a5a5c;
    --ink: #58585a;
    --text-grey: #555557;
    --brand-blue: #1d6db3;
    --brand-blue-light: #3d9ad9;
    --rule: #b8b8ba;
    --white: #ffffff;
  }
  * { box-sizing: border-box; margin: 0; padding: 0; }
  html, body {
    width: 1200px; height: 403px; overflow: hidden;
    background: var(--backdrop);
    font-family: "Source Sans 3", "Helvetica Neue", Arial, sans-serif;
  }
  .canvas { position: relative; width: 1200px; height: 403px; }

  .card {
    position: absolute; top: 48px;
    width: 545px; height: 312px;
    border-radius: 15px; overflow: hidden;
    box-shadow: 0 1px 3px rgba(0,0,0,0.25);
  }
  .card--front { left: 37px; background: var(--card-white); border: 1px solid #7a7a7c; }
  .card--back { left: 619px; background: var(--charcoal); }

  /* name lockup */
  .wordmark { position: absolute; display: flex; align-items: center; gap: 16px; }
  .wordmark__square { width: 70px; height: 62px; background: var(--brand-blue); flex: none; }
  .wordmark__name {
    display: flex; flex-direction: column; font-weight: 600;
    color: var(--ink); line-height: 1;
  }
  .wordmark__main { font-size: 62px; letter-spacing: -1px; }
  .wordmark__sub { font-size: 17px; margin-top: 2px; padding-left: 4px; }
  .card--front .wordmark { left: 112px; top: 36px; }
  .card--back .wordmark { left: 82px; top: 100px; }
  .card--back .wordmark__name { color: var(--white); }
  .card--back .wordmark__main { font-size: 72px; }
  .card--back .wordmark__sub { font-size: 19px; }

  /* contacts */
  .people { position: absolute; top: 127px; left: 0; width: 100%; }
  .person {
    display: flex; justify-content: center; align-items: baseline;
    height: 27px; font-size: 14px; color: var(--text-grey);
    padding-left: 14px;
  }
  .person__name { font-size: 17px; font-weight: 700; color: var(--brand-blue); margin-right: 5px; }
  .person__divider { width: 1px; height: 15px; background: var(--rule); margin: 0 8px; align-self: center; }
  .person__phone { display: inline-flex; align-items: center; gap: 5px; }
  .icon { width: 10px; height: 10px; fill: var(--text-grey); flex: none; }

  .links { position: absolute; top: 198px; left: 0; width: 100%; text-align: center; }
  .link {
    display: flex; justify-content: center; align-items: center; gap: 6px;
    font-size: 14px; color: var(--text-grey); height: 22px; padding-left: 8px;
  }

  .footer-band { position: absolute; left: 0; bottom: 0; width: 545px; height: 52px; }
  .address {
    position: absolute; left: 289px; bottom: 14px;
    font-size: 13.5px; color: var(--white);
  }

  .web-back {
    position: absolute; top: 238px; left: 0; width: 100%; text-align: center;
    font-size: 13.5px; letter-spacing: 1.2px; color: var(--white);
  }
</style>
</head>
<body>
<main class="canvas">

  <section class="card card--front" aria-label="Card front">
    <div class="wordmark">
      <span class="wordmark__square"></span>
      <span class="wordmark__name">
        <span class="wordmark__main">Corwen</span>
        <span class="wordmark__sub">Property Management</span>
      </span>
    </div>

    <div class="people">
      <p class="person">
        <span class="person__name">Dean Fosterly,</span> Principal
        <span class="person__divider"></span>
        <span class="person__phone">
          <svg class="icon" viewBox="0 0 10 10"><path d="M2 0.5 L3.6 2.6 L2.7 3.6 C3.3 5 4.9 6.6 6.4 7.3 L7.4 6.4 L9.5 8 L8.4 9.5 C4.5 9.2 0.8 5.5 0.5 1.6 Z"/></svg>
          0419 372 508
        </span>
      </p>
      <p class="person">
        <span class="person__name">Tessa Fosterly,</span> Director
        <span class="person__divider"></span>
        <span class="person__phone">
          <svg class="icon" viewBox="0 0 10 10"><path d="M2 0.5 L3.6 2.6 L2.7 3.6 C3.3 5 4.9 6.6 6.4 7.3 L7.4 6.4 L9.5 8 L8.4 9.5 C4.5 9.2 0.8 5.5 0.5 1.6 Z"/></svg>
          0419 613 947
        </span>
      </p>
    </div>

    <div class="links">
      <p class="link">
        <svg class="icon" viewBox="0 0 10 8"><path d="M0 0 H10 V1 L5 4 L0 1 Z M0 2 L5 5 L10 2 V8 H0 Z"/></svg>
        admin@corwenpropertymanagement.com.au
      </p>
      <p class="link">
        <svg class="icon" viewBox="0 0 10 10"><circle cx="5" cy="5" r="5"/></svg>
        www.corwenpropertymanagement.com.au
      </p>
    </div>

    <svg class="footer-band" viewBox="0 0 545 52" aria-hidden="true">
      <defs>
        <linearGradient id="stripe-blue" x1="0" x2="1" y1="0" y2="0">
          <stop offset="0" stop-color="var(--brand-blue)"/>
          <stop offset="1" stop-color="var(--brand-blue-light)"/>
        </linearGradient>
      </defs>
      <polygon points="0,5 262,5 250,19 0,19" fill="url(#stripe-blue)"/>
      <polygon points="271,0 545,0 545,52 0,52 0,26 249,26" fill="var(--charcoal)"/>
    </svg>
    <p class="address">PO Box 718, Holloway SA 5093</p>
  </section>

  <section class="card card--back" aria-label="Card back">
    <div class="wordmark">
      <span class="wordmark__square"></span>
      <span class="wordmark__name">
        <span class="wordmark__main">Corwen</span>
        <span class="wordmark__sub">Property Management</span>
      </span>
    </div>
    <p class="web-back">www.corwenpropertymanagement.com.au</p>
  </section>

</main>
</body>
</html>
```